Web Site Redesign for Quellorainc.example

- Introduction

This is a web site redesign content. Please follow the following instructions. I am on tight schedule, so instead of 10 days, I would like to select the final design within 7 days. After the final design is selected, I would like the winner to produce the static HTML pages, but that is a separate job.

Delivery is JPG, complete Layered PSD files, and color numbers used in the design.

- Language of Content of the Web Site: English

- Company Name: Quellora, Inc.

- What is Quellora, Inc.'s product? Company develops and markets a sophisticated engineering simulation software.

- URL of existing web site: http://www.quellorainc.example

- Purpose of the web site: Marketing Engineering and Simulation Software

- Markets/Industries served

1. Medical: Radiotheraphy, Cancer Therapy, Medical Imaging
2. Energy: Nuclear Physics
3. National Security: Dept. of Coastal Surveying

- Three most important messages to communicate to our audience:

1. A solid and sophisticated engineering company (sophisticated).
2. A company with cutting-edge technology and leading products (cutting edge)
3. A company with state-of-art, live and professional marketing (state-of-the-art and live)

- What differentiates Quellora, Inc. from other competitors?

1. We are a commercial company vs. a home-grown entity with competitor products.
2. Our software is in-depth and targeted application vs. a general software with certain capabilities.

- Desired homepage screen size: 1280x800 or use your best recommendation.

- Number of templates: 2
1. Homepage
2. Secondary pages

- What content must be included in the Homepage (video, slideshow, etc.)?

1. Header block to display the logo, company name, and login or registration space (if user is logged in, show username)
2. One primary block to display a slide presentation (in HTML5, up to 4 or 5 slides with combined image and text)
3. One block to display a video and ability to play the video with a link "More" to go to the Video Training page.
4. One block to display announcements and special events
5. One block to display up to three News/Events. A Caption and Date.
6. One block to showcase links to three social networks: Chatterfold, Workloom, and Pipsqueal.
7. One block for Footer. Standard links and copyright notice

- Describe secondary pages: They will include text and images (JPG or PNG). A Training page will display a list of (up to 5) video clips.

- Site Menu Structure

1. Top Level. Up to 6 main menu as follows: Products, Support, Partners, Company, News/Events, and Purchase.

2. Second Level. Each top-level menu could have up to 4 sub-menu options. Some like Partners will not have any page. You don't have to display Third-level menus here.

3. Third Level. Some second-level menu items could have from up to 4 sub-menu options. Third-level menu options should appear in the template for secondary pages.

For example, under main menu "Products" we have three products one of which is "Borvek3QXRT." This product will have 4 options (4 pages). The template for the secondary pages should be flexible enough to allow for more than 4 but less than 6-7 options for each product.

(I will upload the Site Map document shortly)

- Style/theme of the Website:
1. Large enough font size. Audience is 30 and older.
2. Appealing to users of a highly-sophisticated desktop-based simulation software

- Desirable colors in the new design: Blue (because of logo), red, green, gray, black. White or Black background

- Adjectives that should best describe the new design: Welcoming, exciting, informative, and professional

- Websites you like (because?):

http://www.mendalux.example. Only because they also develop sophisticated software and they follow a similar licensing scheme, but PLEASE do not copy their UI.

Target Market(s)

- Age: 30 years and older
- Mostly male.
- Job Title: Researchers, Doctors, and Engineers
- Users of radiotheraphy, cancer therapy, medical imaging, nuclear energy, and homeland security radiation simulation software

Industry/Entity Type

Marketing

Requirements
Must have
• - What content must be included in the Homepage (video, slideshow, etc.)?

7. One block for Footer. Standard links and copyright notice.
Nice to have
• As you see I gave a thorough and detail design brief (I hope so). I leave it to you to incorporate "nice to haves" in your design.
Should not have
• - No Cartoonish Design or Animation
- Colors we do you NOT like: Purple, Pink, Yellow, Brown

```html
<!DOCTYPE html>
<html lang="en">
<head>
<meta charset="utf-8">
<title>Quellora, Inc. — Radiation Transport Simulations</title>
<link rel="stylesheet" href="https://fonts.googleapis.com/css2?family=Archivo+Narrow:wght@400;500;700&family=Open+Sans:wght@400;600;700&display=swap">
<style>
:root{
  --blue:#1f5fc4;
  --blue-deep:#0d2f86;
  --blue-bright:#2a74e0;
  --navy:#0a1a3c;
  --red:#c8342b;
  --red-dark:#a82a22;
  --green:#2fa52a;
  --header-bg:#ececec;
  --black:#000;
  --panel:#1e1e1e;
  --panel-line:#3a3a3a;
  --text-grey:#8a8a8a;
  --text-light:#d0d0d0;
  --link:#4f93f0;
  --white:#fff;
  --footer:#1a1a1a;
}
*{box-sizing:border-box;margin:0;padding:0}
html,body{width:877px;height:1200px;overflow:hidden;background:var(--black)}
body{position:relative;font-family:"Open Sans",Arial,sans-serif;color:var(--text-grey)}
.abs{position:absolute}

/* header */
.site-header{left:0;top:0;width:877px;height:80px;background:var(--header-bg)}
.brand{left:40px;top:22px;display:flex;align-items:center;gap:10px}
.brand-mark{width:30px;height:30px;background:var(--blue-deep)}
.brand-name{font-family:"Archivo Narrow",sans-serif;font-weight:700;font-size:22px;letter-spacing:4px;color:#111;line-height:1}
.brand-tag{left:86px;top:46px;font-size:11px;font-weight:700;letter-spacing:1.6px;color:#111}
.social{left:440px;top:14px;display:flex;gap:10px}
.social-item{display:flex;align-items:center;gap:4px;font-size:9px;font-weight:600;color:#555}
.social-item i{width:9px;height:9px;background:var(--blue-deep);display:block}
.search{left:520px;top:47px;width:135px;height:22px;background:#2b2b2b;border-radius:2px;font-size:9px;font-style:italic;color:#888;padding:5px 8px}
.search-btn{left:630px;top:45px;width:26px;height:26px;background:var(--blue);transform:rotate(45deg)}
.account{left:680px;top:0;width:156px;height:78px;background:var(--red)}
.field{left:693px;width:130px;height:19px;border:1px solid #e2574e;background:var(--red-dark);font-size:9px;color:#fff;padding:3px 7px}
.btn-small{top:62px;height:16px;background:var(--blue-deep);color:#fff;font-size:10px;font-weight:700;font-style:italic;text-align:center;line-height:16px;border-radius:1px}
.forgot{left:694px;top:86px;font-size:9px;color:#fff}

/* nav */
.main-nav{left:0;top:80px;width:877px;height:30px;background:var(--red);display:flex;padding-left:40px}
.nav-item{font-family:"Archivo Narrow",sans-serif;font-size:13px;color:#f3d0cd;height:30px;line-height:30px;padding:0 19.5px;border-right:1px solid #b72d25}
.nav-item.active{background:var(--blue);color:#fff}

/* hero */
.hero-visual{left:0;top:110px;width:551px;height:320px;background:
  radial-gradient(ellipse 140px 110px at 64% 50%,rgba(120,220,255,.55) 0%,rgba(60,150,240,.25) 55%,transparent 100%),
  radial-gradient(ellipse 70px 130px at 23% 50%,rgba(110,210,255,.45) 0%,transparent 100%),
  linear-gradient(115deg,rgba(255,255,255,.08) 0%,transparent 40%),
  radial-gradient(circle at 60% 45%,#2f7fe6 0%,#1a56bf 55%,#0f3a8f 100%)}
.hero-edge{left:836px;top:110px;width:41px;height:320px;background:linear-gradient(#1e5fc4,#153f8f)}
.hero-copy{left:551px;top:110px;width:285px;height:320px;background:radial-gradient(ellipse at 30% 30%,#13306a 0%,#0a1c45 60%,#06122c 100%)}
.hero-title{left:573px;top:143px;font-family:"Archivo Narrow",sans-serif;font-weight:500;font-size:33px;color:#fff}
.hero-text{left:573px;top:197px;width:252px;font-size:12px;line-height:19.2px;color:#e6e9f2}
.btn{top:357px;height:25px;font-family:"Archivo Narrow",sans-serif;font-weight:500;font-size:12px;color:#fff;text-align:center;line-height:23px;border:1px solid rgba(255,255,255,.35)}
.btn-contact{left:575px;width:75px;background:var(--red)}
.btn-more{left:660px;width:76px;background:var(--green)}

/* welcome */
.welcome-title{left:40px;top:449px;font-family:"Archivo Narrow",sans-serif;font-weight:400;font-size:20px;color:var(--blue-bright)}
.welcome-rule{left:40px;top:479px;width:580px;height:1px;background:#222}
.welcome-text{left:40px;top:486px;width:580px;font-size:11.6px;line-height:17.4px;color:#7a7a7a;letter-spacing:-.1px}
.video{left:644px;top:454px;width:191px;height:131px;border:2px solid var(--blue);background:
  radial-gradient(ellipse 40px 30px at 70% 15%,#d9a05c 0%,transparent 100%),
  radial-gradient(ellipse 70px 40px at 40% 55%,#7ccf7a 0%,transparent 100%),
  linear-gradient(120deg,#12307a 0%,#2f7fcf 45%,#4aa8c8 70%,#1b3f95 100%)}

/* cards */
.card{top:609px;width:240px;height:272px;background:#fff;border-bottom:3px solid var(--blue)}
.card-media{width:238px;height:164px;margin:1px}
.card-title{font-family:"Archivo Narrow",sans-serif;font-weight:400;font-size:21px;color:var(--blue);margin:4px 0 0 14px;line-height:26px}
.card-text{font-size:10.6px;line-height:15.5px;color:#8a8a8a;margin:2px 14px 0 14px;letter-spacing:-.1px}
.card-corner{position:absolute;right:0;bottom:0;width:0;height:0;border-left:22px solid transparent;border-bottom:22px solid var(--blue)}

/* panels */
.panel{top:905px;width:378px;height:218px;background:var(--panel)}
.panel-head{height:33px;background:var(--blue);color:#fff;font-family:"Archivo Narrow",sans-serif;font-size:20px;padding:3px 0 0 11px;position:relative}
.panel-icon{position:absolute;right:12px;top:6px;width:22px;height:22px;background:#fff;border-radius:50%}
.entry{margin:0 24px 0 12px;padding:9px 0 7px 0;border-bottom:1px dashed var(--panel-line);font-size:9.6px;line-height:13px;color:var(--text-light)}
.entry.current{border-left:2px solid var(--blue);margin-left:0;padding-left:10px}
.entry:last-child{border-bottom:none}
.meta{margin-top:3px;font-size:10.5px;font-weight:700;color:#fff;word-spacing:2px}
.meta .when{color:var(--link);font-weight:400}
.news-meta{margin-top:3px;font-size:10px;color:#888}
.news-meta b{color:var(--link);font-weight:400}
.scroll{position:absolute;right:6px;top:42px;width:5px;height:164px;background:#3a3a3a;border-radius:3px}
.scroll::after{content:"";position:absolute;top:0;left:0;width:5px;height:16px;background:var(--blue);border-radius:3px}

/* footer */
.site-footer{left:0;top:1147px;width:877px;height:53px;background:var(--footer)}
.footer-address{left:0;top:1155px;width:877px;text-align:center;font-size:11px;color:#555}
.footer-address a{color:var(--link);font-weight:700;text-decoration:none}
.footer-links{left:40px;top:1176px;display:flex;font-size:10px;color:#555}
.footer-links span{padding:0 8px;border-left:1px solid #333}
.footer-links span:first-child{padding-left:0;border-left:none;color:var(--link)}
.copyright{right:41px;top:1176px;font-size:10px;color:#555}
</style>
</head>
<body>

<header class="abs site-header"></header>
<div class="abs brand"><span class="brand-mark"></span><span class="brand-name">QUELLORA INC.</span></div>
<div class="abs brand-tag">Radiation Transport Simulations</div>

<div class="abs social">
  <span class="social-item"><i></i>Chatterfold</span>
  <span class="social-item"><i></i>Pipsqueal</span>
  <span class="social-item"><i></i>Workloom</span>
</div>
<div class="abs search">Search...</div>
<div class="abs search-btn"></div>

<div class="abs account"></div>
<div class="abs field" style="top:8px">Username:</div>
<div class="abs field" style="top:33px">Password:</div>
<div class="abs btn-small" style="left:693px;width:45px">LOGIN</div>
<div class="abs btn-small" style="left:746px;width:59px">REGISTER</div>
<div class="abs forgot">Forgot password</div>

<nav class="abs main-nav">
  <span class="nav-item active">HOME</span>
  <span class="nav-item">PRODUCTS</span>
  <span class="nav-item">SUPPORT</span>
  <span class="nav-item">PARTNERS</span>
  <span class="nav-item">COMPANY</span>
  <span class="nav-item">NEWS/EVENTS</span>
  <span class="nav-item">PURCHASE</span>
</nav>

<div class="abs hero-visual" role="img" aria-label="Radiation dose simulation visual with isodose contours"></div>
<div class="abs hero-edge"></div>
<div class="abs hero-copy"></div>
<h1 class="abs hero-title">VELTRAN</h1>
<p class="abs hero-text">Lorem ipsum dolor sit amet, consectetur adipiscing elit. Praesent ac facilisis nunc. Aliquam suscipit nisl magna. Nunc ac orci eget eros sodales hendrerit a a nulla. Donec in vulputate neque. Maecenas ac vehicula urna, ac pellentesque quam. Aliquam rutrum metus vestibulum</p>
<div class="abs btn btn-contact">CONTACT US</div>
<div class="abs btn btn-more">READ MORE</div>

<h2 class="abs welcome-title">WELCOME TO OUR SITE!</h2>
<div class="abs welcome-rule"></div>
<p class="abs welcome-text">Lorem ipsum dolor sit amet, consectetur adipiscing elit. Praesent ac facilisis nunc. Aliquam suscipit nisl magna. Nunc ac orci eget eros sodales hendrerit a a nulla. Donec in vulputate neque. Maecenas ac vehicula urna, ac pellentesque quam. Aliquam rutrum metus vestibulum dolor porta volutpat sed eget orci. Sed sed diam id massa dictum mollis a non augue. Nulla et risus nibh. Duis vitae sem quis ipsum mollis ullamcorper ac id felis. Nulla malesuada ac lectus vel fermentum. Ut sit amet tellus elementum ligula sollicitudin sodales non porttitor lacus.</p>
<div class="abs video" role="img" aria-label="Video still of a dose distribution simulation"></div>
<svg class="abs" style="left:718px;top:497px" width="44" height="44" viewBox="0 0 44 44">
  <circle cx="22" cy="22" r="20" fill="#1f5fc4" stroke="#fff" stroke-width="3"/>
  <path d="M17 13 L31 22 L17 31 Z" fill="#fff"/>
</svg>

<article class="abs card" style="left:40px">
  <div class="card-media" role="img" aria-label="Isodose contour simulation on black" style="background:radial-gradient(ellipse 90px 60px at 52% 48%,rgba(255,140,90,.55) 0%,rgba(60,200,255,.35) 45%,transparent 100%),radial-gradient(ellipse 120px 80px at 50% 50%,#1d3f8a 0%,#0a1430 60%,#020408 100%)"></div>
  <h3 class="card-title">Markets Industries served</h3>
  <p class="card-text">Lorem ipsum dolor sit amet, consectetur adipiscing elit. Fusce semper enim in eros vestibulum condimentum. Donec sceleris- que convallis est ac commodo.</p>
  <span class="card-corner"></span>
</article>
<article class="abs card" style="left:318px">
  <div class="card-media" role="img" aria-label="Support staff with headsets at computers" style="background:radial-gradient(ellipse 80px 90px at 70% 45%,#f6f2ee 0%,transparent 100%),radial-gradient(ellipse 60px 40px at 20% 75%,#5d6670 0%,transparent 100%),linear-gradient(135deg,#b9c2cc 0%,#e4e8ec 45%,#f3f5f7 65%,#c7ced6 100%)"></div>
  <h3 class="card-title">Communicate</h3>
  <p class="card-text">Lorem ipsum dolor sit amet, consectetur adipiscing elit. Fusce semper enim in eros vestibulum condimentum. Donec sceleris- que convallis est ac commodo.</p>
  <span class="card-corner"></span>
</article>
<article class="abs card" style="left:596px">
  <div class="card-media" role="img" aria-label="Tablet showing colourful analytics charts" style="background:radial-gradient(ellipse 70px 50px at 40% 40%,rgba(230,80,110,.35) 0%,transparent 100%),linear-gradient(125deg,#f2f2f4 0%,#d4d7dc 50%,#6a6e76 72%,#8d4fa0 84%,#e0b030 90%,#2a8fd0 100%)"></div>
  <h3 class="card-title">What differentiates</h3>
  <p class="card-text">Lorem ipsum dolor sit amet, consectetur adipiscing elit. Fusce semper enim in eros vestibulum condimentum. Donec sceleris- que convallis est ac commodo.</p>
  <span class="card-corner"></span>
</article>

<section class="abs panel" style="left:40px">
  <div class="panel-head">Latest Posts<span class="panel-icon"></span></div>
  <div class="entry current">Lorem ipsum dolor sit amet, consectetur adipiscing elit. Praesent ac facilisis nunc. Aliquam suscipit<div class="meta"><span class="when">2 hours ago</span> · reply · retweet · favrite</div></div>
  <div class="entry">Lorem ipsum dolor sit amet, consectetur adipiscing elit. Praesent ac facilisis nunc. Aliquam suscipit<div class="meta">2 hours ago · reply · retweet · favrite</div></div>
  <div class="entry">Lorem ipsum dolor sit amet, consectetur adipiscing elit. Praesent ac facilisis nunc. Aliquam suscipit<div class="meta">2 hours ago · reply · retweet · favrite</div></div>
  <span class="scroll"></span>
</section>

<section class="abs panel" style="left:458px">
  <div class="panel-head">Recent News
    <svg style="position:absolute;right:10px;top:5px" width="28" height="24" viewBox="0 0 28 24" fill="none" stroke="#fff" stroke-width="1.5">
      <path d="M2 14 L14 8 L26 14 L14 20 Z"/><path d="M2 17 L14 23 L26 17"/><path d="M2 11 L14 5 L26 11"/>
    </svg>
  </div>
  <div class="entry current">Lorem ipsum dolor sit amet, consectetur adipiscing elit Curabitur at dolor faucibus feugiat purus non dapibus.<div class="news-meta"><b>Date:</b> 10 / 07 / 2013 &nbsp;&nbsp;|&nbsp;&nbsp; <b>Time:</b> 6: pm &nbsp;&nbsp;|&nbsp;&nbsp; <b>Caption:</b> Loremispum</div></div>
  <div class="entry">Lorem ipsum dolor sit amet, consectetur adipiscing elit Curabitur at dolor faucibus feugiat purus non dapibus.<div class="news-meta"><b>Date:</b> 10 / 07 / 2013 &nbsp;&nbsp;|&nbsp;&nbsp; <b>Time:</b> 6: pm &nbsp;&nbsp;|&nbsp;&nbsp; <b>Caption:</b> Loremispum</div></div>
  <div class="entry">Lorem ipsum dolor sit amet, consectetur adipiscing elit Curabitur at dolor faucibus feugiat purus non dapibus.<div class="news-meta"><b>Date:</b> 10 / 07 / 2013 &nbsp;&nbsp;|&nbsp;&nbsp; <b>Time:</b> 6: pm &nbsp;&nbsp;|&nbsp;&nbsp; <b>Caption:</b> Loremispum</div></div>
  <span class="scroll"></span>
</section>

<footer class="abs site-footer"></footer>
<p class="abs footer-address">Quellora, Inc. 4120 Harrow Ln. Suite B210, Fernmoor, WA 98000 • 555.014.2290 • <a href="#">info@quellorainc.example</a></p>
<div class="abs footer-links"><span>Home</span><span>Support</span><span>Contact Us</span><span>Terms of Use</span><span>Privacy Policy</span><span>License Agreement</span></div>
<p class="abs copyright">Copyright 2004 - 2013 by Quellora, Inc. - All Rights Reserved</p>

</body>
</html>
```